Postcard Design

We have a chiropractic office.

We'd need our logo, main message / title being about our new hours, a call to action with a coupon or two, a doctor picture, announcement that we accept all insurance (except for medicaid), our wellness lecture schedule

New Hours:
Monday 9:00 - 1:00 3:00 - 6:00
Tuesday 3:00 - 6:00
Wednesday 9:00 - 1:00 3:00 - 6:00
Thursday 3:00 - 6:00
Friday 9:00 - 1:00 3:00 - 6:00

or could say:
Monday, Wednesday, Friday 9:00 - 1:00 3:00 - 6:00
and Tuesday / Thursday 3:00 - 6:00

Trigger Point Workshop!
Tuesday, October 21, 6:30 p.m.
Learn how to find and release those sore spots in your muscles. Dr. Halvorsen will educate you on how to find trigger points and how to help them heal. Great for people with headaches, neck and shoulder pain, lower back and hip pain. Bring a guest/partner and RSVP at (555) 417-3086.

Coupon:
Refer a friend: Free Pain Consultation and Assessment.

Coupon:
$20 off a 30 minute massage and Chiropractic Adjustment combo. Must have coupon present. Call clinic to schedule your "combo".

Website: brightpathcx.com

Pain Relief and Wellness Start Here

Target Market(s)

our current patient base

Industry/Entity Type

Insurance

Font styles to use
Other font styles liked:
• clean and modern and bold, not "script" or "decorative"

Colors
cadf82
85cae6
fdce3e

Requirements
Must have
• Ability to be mailed with a place for return address, address label and area for postage meter stamp

Return address:
4173 W Marlowe St, Broken Arrow, OK 74012

clean look, eye catching title, easy to read

ability to make old patients want to call us

Color scheme below are only suggestions but feel free to make it however you want. Perhaps a white background keeps it cleaner.

```html
<!DOCTYPE html>
<html lang="en">
<head>
<meta charset="utf-8">
<title>Brightpath Chiropractic Postcard</title>
<link href="https://fonts.googleapis.com/css2?family=Roboto:ital,wght@0,400;0,500;0,700;1,400&family=Arimo:wght@400;700&display=swap" rel="stylesheet">
<style>
  :root {
    --green: #cadf82;
    --blue: #85cae6;
    --yellow: #fdce3e;
    --panel: #dddddd;
    --ink: #1d1d1d;
    --frame: #333333;
    --paper: #ffffff;
  }
  * { margin: 0; padding: 0; box-sizing: border-box; }
  html, body { width: 1200px; height: 900px; overflow: hidden; background: var(--paper); }
  .sheet { position: relative; width: 1200px; height: 900px; font-family: "Roboto", Arial, sans-serif; color: var(--ink); }
  .side-label { position: absolute; left: 332px; font-family: "Arimo", Arial, sans-serif; font-size: 18px; }
  .card { position: absolute; left: 441px; width: 403px; height: 312px; border: 1px solid var(--frame); background: var(--paper); overflow: hidden; }
  .card--front { top: 121px; }
  .card--back { top: 476px; }
  .tile { position: absolute; width: 21px; height: 21px; }
  .tile--g { background: var(--green); }
  .tile--b { background: var(--blue); }
  .tile--y { background: var(--yellow); }

  .workshop { position: absolute; left: 0; top: 0; width: 403px; height: 86px; background: var(--green); }
  .doctor-photo { position: absolute; left: 9px; top: 9px; width: 53px; height: 74px; background: linear-gradient(160deg, #9a8f86, #3e3d44 70%, #2b2f3a); }
  .workshop-copy { position: absolute; left: 72px; top: 8px; width: 310px; font-size: 8.4px; line-height: 11px; }
  .workshop-title { font-weight: 700; font-size: 10.2px; line-height: 13px; margin-bottom: 2px; }
  .workshop-copy strong { font-weight: 500; }

  .coupon { position: absolute; background: var(--panel); font-size: 9.6px; line-height: 12.3px; }
  .coupon-title { font-weight: 700; }
  .coupon--referral { left: 42px; top: 92px; width: 137px; height: 84px; padding: 16px 0 0 15px; }
  .coupon--combo { left: 201px; top: 135px; width: 180px; height: 93px; padding: 15px 0 0 14px; }
  .coupon--combo strong { font-weight: 500; }

  .hours { position: absolute; left: 0; top: 249px; width: 201px; height: 63px; background: var(--yellow); padding: 13px 0 0 10px; font-size: 7.9px; line-height: 10px; }
  .hours-title { font-size: 10px; font-weight: 700; line-height: 13px; }
  .hours em { font-style: italic; }
  .tagline { position: absolute; left: 201px; top: 249px; width: 202px; height: 63px; background: var(--blue); padding: 25px 0 0 10px; font-size: 10px; line-height: 12px; font-weight: 500; }

  .brand-name { position: absolute; left: 26px; top: 146px; font-family: "Roboto", Arial, sans-serif; font-size: 22px; font-weight: 400; color: var(--blue); line-height: 24px; }
  .return-address { position: absolute; left: 215px; top: 152px; font-family: "Arimo", Arial, sans-serif; font-size: 10px; line-height: 12px; }
  .return-address-title { font-weight: 700; }
</style>
</head>
<body>
<div class="sheet">
  <div class="side-label" style="top:118px">Front:</div>
  <section class="card card--front">
    <div class="workshop">
      <div class="doctor-photo" role="img" aria-label="Portrait photo of Dr. Halvorsen"></div>
      <div class="workshop-copy">
        <div class="workshop-title">Trigger Point Workshop! Tuesday, October 21, 6:30 p.m.</div>
        Learn how to find and release those sore spots in your muscles.<br>
        Dr. Halvorsen will educate you on how to find trigger points and how to help them heal. Great for people with <strong>headaches, neck and shoulder pain, lower back and hip pain.</strong><br>
        Bring a guest/partner and RSVP at (555) 417-3086.
      </div>
    </div>
    <div class="tile tile--y" style="left:381px;top:50px"></div>
    <div class="tile tile--b" style="left:360px;top:71px"></div>
    <div class="tile tile--g" style="left:381px;top:71px"></div>
    <div class="tile tile--g" style="left:381px;top:92px"></div>
    <div class="tile tile--y" style="left:0;top:92px"></div>
    <div class="tile tile--g" style="left:21px;top:92px"></div>
    <div class="tile tile--g" style="left:0;top:113px"></div>
    <div class="tile tile--b" style="left:0;top:134px"></div>
    <div class="tile tile--g" style="left:21px;top:134px"></div>
    <div class="tile tile--y" style="left:21px;top:155px"></div>
    <div class="tile tile--g" style="left:21px;top:176px"></div>
    <div class="tile tile--y" style="left:42px;top:176px"></div>
    <div class="tile tile--b" style="left:63px;top:176px"></div>
    <div class="tile tile--y" style="left:42px;top:197px;background:var(--green)"></div>
    <div class="tile tile--g" style="left:158px;top:207px"></div>
    <div class="tile tile--b" style="left:111px;top:228px"></div>
    <div class="tile tile--y" style="left:0;top:228px"></div>
    <div class="tile tile--g" style="left:179px;top:155px"></div>
    <div class="tile tile--y" style="left:223px;top:92px"></div>
    <div class="tile tile--g" style="left:244px;top:92px"></div>
    <div class="tile tile--b" style="left:244px;top:113px"></div>
    <div class="tile tile--g" style="left:265px;top:113px"></div>
    <div class="tile tile--y" style="left:338px;top:113px"></div>
    <div class="tile tile--b" style="left:360px;top:134px"></div>
    <div class="tile tile--g" style="left:381px;top:155px"></div>
    <div class="tile tile--b" style="left:201px;top:228px"></div>
    <div class="tile tile--g" style="left:244px;top:228px"></div>
    <div class="tile tile--y" style="left:265px;top:249px;z-index:2"></div>

    <div class="coupon coupon--referral">
      <div class="coupon-title">COUPON #1</div>
      Refer a friend<br>Free Pain Consultation<br>and Assessment.
    </div>
    <div class="coupon coupon--combo">
      <div class="coupon-title">COUPON #2</div>
      $20 off a 30 minute massage and<br><strong>Chiropractic Adjustment combo.</strong><br>Must have coupon present. Call<br>clinic to schedule your "<em>combo</em>".
    </div>
    <div class="hours">
      <div class="hours-title">New Opening Hours</div>
      Monday, Wednesday, Friday 9:00 - 1:00 &nbsp;3:00 - 6:00<br>
      Tuesday / Thursday 3:00 - 6:00<br>
      <em>All insurances accepted, except medicaid</em>
    </div>
    <div class="tagline">Pain Relief and Wellness Start Here:<br>brightpathcx.com</div>
  </section>

  <div class="side-label" style="top:475px">Back:</div>
  <section class="card card--back">
    <div class="tile tile--y" style="left:10px;top:9px"></div>
    <div class="tile tile--g" style="left:31px;top:9px"></div>
    <div class="tile tile--b" style="left:31px;top:30px"></div>
    <div class="tile tile--g" style="left:52px;top:30px"></div>
    <div class="tile tile--g" style="left:119px;top:9px"></div>
    <div class="tile tile--b" style="left:214px;top:51px"></div>
    <div class="tile tile--y" style="left:119px;top:72px"></div>
    <div class="tile tile--g" style="left:193px;top:72px"></div>
    <div class="tile tile--y" style="left:278px;top:72px"></div>

    <div class="brand-name">Brightpath<br>Chiropractic</div>
    <div class="return-address">
      <div class="return-address-title">Return Address:</div>
      Brightpath Chiropractic<br>4173 W Marlowe St<br>Broken Arrow, OK 74012
    </div>
  </section>
</div>
</body>
</html>
```